brevakor.com

I have a site already disigned, however at the time I had no clue of how and what my site should look like. Still pretty cluless but I know I need to make some fundamenlal changes. I'm looking fora designer who understands how to connect with the cosumer with a ballance of visual and content with SEO in mind.I have a lot of content ready to be added to the mix, just missing alot of bottons for the content for example I have FAQ content but no FAQ botton. There are a lot of things I would like to add and take away from the current site. Here is a list of what I would like to add and subtracted from the site.Take away the find botton and ad contact us change the about botton to about brevakor,under that botton i want bottons that lead to News/Events,carreer opertunities,contact us and priacy policy. I also want to add Services offered: personal training,Motivational speeking ,bootcamp conditioning,rondalo,kickboxing cardio,and hip hop cordio. I want to add a botton for testimonials:video and written. I need to add a blog botton, a FAQ botton, and before and after. I want to add a social media botton: chatterloop, snapvelle,quibbler,hirenook,clipstream,and map corner. I need to add a store botton; T shirts. I would like the contact info the be linked to my email. and I would like would like at the top of contact form to read Request a free info session Now!!! But I don't need a new design I need to add these thing to the one I already have whitch is CMS based

Reason: I need my site to have new logo, just figured out how to down load logo

Reason: I need site to be CMS based so I can up load content and pics

Target Market(s)

People who want to loose weight, mostley women over the age of 30 and men over the age of 40 that income is at least 60,000 a year

Industry/Entity Type

Store

Font styles to use
Sans Serif
Decorative

Colors
000000
ec1f27
0255a3

Requirements
Must have
• Adding the drop downs listed above

```html
<!DOCTYPE html>
<html lang="en">
<head>
<meta charset="utf-8">
<title>Brevakor Fitness</title>
<link href="https://fonts.googleapis.com/css2?family=Ubuntu:wght@400;500;700&display=swap" rel="stylesheet">
<style>
:root{
  --black:#000000;
  --red:#ec1f27;
  --blue:#0255a3;
  --panel:#f4f4f4;
  --text:#222222;
  --muted:#777777;
  --line:#d6d6d6;
}
*{box-sizing:border-box;margin:0;padding:0}
html,body{width:1076px;height:1200px;overflow:hidden}
body{position:relative;font-family:'Ubuntu',sans-serif;color:var(--text);background:#3a3a3a}
.backdrop{position:absolute;left:0;top:119px;width:1076px;height:1081px;
  background:radial-gradient(ellipse at 40% 70%,#2a4f8f 0%,#1f3f78 30%,#444 65%,#2a2a2a 100%)}
.site-header{position:absolute;left:0;top:0;width:1076px;height:119px;
  background:linear-gradient(#1c1c1c,#0b0b0b);border-bottom:2px solid #5a1214}
.brand{position:absolute;left:95px;top:34px;display:flex;align-items:center;gap:10px}
.brand-mark{width:30px;height:30px;border-radius:50%;background:#9a9a9a}
.brand-name{font-size:38px;font-weight:500;color:#9a9a9a;line-height:42px}
.follow{position:absolute;right:98px;top:12px;display:flex;align-items:center;gap:5px;font-size:11px;color:#aaa}
.follow span{margin-right:4px}
.dot{width:22px;height:22px;border-radius:50%;background:#fff;display:inline-block}
.search{position:absolute;left:780px;top:47px;width:199px;height:27px;background:#fff;border-radius:3px;
  font-size:11px;color:#888;padding:7px 10px}
.search svg{position:absolute;right:8px;top:5px}
.main-nav{position:absolute;right:98px;top:87px;display:flex;font-size:12px;font-weight:700;color:#fff}
.main-nav a{padding:0 9px;border-left:1px solid #444;color:#fff;text-decoration:none}
.main-nav a:first-child{border:0;color:var(--red)}
.main-nav a:last-child{padding-right:0}
.panel{position:absolute;background:var(--panel)}
.panel-title{position:absolute;left:0;top:-34px;height:34px;color:#fff;font-size:19px;font-weight:500;
  padding:7px 12px;background:linear-gradient(#3a3a3a,#000);clip-path:polygon(0 0,80% 0,100% 100%,0 100%)}
.corner{position:absolute;right:0;bottom:0;width:28px;height:28px;background:var(--red);
  clip-path:polygon(100% 0,100% 100%,0 100%)}
.corner::after{content:"+";position:absolute;right:4px;bottom:-1px;color:#fff;font-size:13px;font-weight:700}
.contact{left:94px;top:132px;width:261px;height:359px;background:#fff}
.contact .bar{position:absolute;left:0;top:0;width:261px;height:36px;background:linear-gradient(#3a3a3a,#050505);
  color:#fff;font-size:19px;font-weight:500;padding:7px 20px}
.field{position:absolute;left:17px;width:224px;height:27px;border:1px solid #bbb;border-radius:4px;
  font-size:11px;color:#666;padding:6px 13px}
.field.select::after{content:"";position:absolute;right:12px;top:10px;border:4px solid transparent;border-top:6px solid #888}
.field.msg{height:76px}
.btn{position:absolute;background:var(--red);color:#fff;font-size:12px;font-weight:700;border-radius:3px;
  text-align:center;line-height:25px}
.slider{position:absolute;left:373px;top:133px;width:605px;height:358px;background:#555;padding:5px}
.slide{width:100%;height:100%;background:linear-gradient(135deg,#7a2a2a 0%,#5a4a44 35%,#2c5aa8 55%,#888 80%,#444 100%)}
.arrow{position:absolute;top:161px;width:28px;height:28px;border:2px solid #fff;border-radius:50%}
.arrow svg{position:absolute;left:7px;top:6px}
.services{left:94px;top:543px;width:281px;height:176px}
.services ul{list-style:none;padding:10px 18px 0 18px}
.services li{font-size:11.5px;height:25px;line-height:25px;border-bottom:1px solid var(--line);display:flex;align-items:center}
.services li:last-child{border:0}
.services li i{width:10px;height:10px;border:1.5px solid #777;border-radius:50%;margin-right:14px;display:inline-block}
.gallery{left:395px;top:543px;width:281px;height:176px}
.thumb{position:absolute;width:71px;height:60px;background:linear-gradient(135deg,#8a3a30,#3464b0 55%,#999)}
.thumb.alt{background:linear-gradient(135deg,#555,#2458b5 60%,#777)}
.training{left:697px;top:543px;width:281px;height:176px}
.prog{position:absolute;left:18px;width:250px}
.prog .thumb{position:static;float:left;margin-right:11px}
.prog h4{font-size:12px;font-weight:700;margin-bottom:3px}
.prog p{font-size:11.5px;line-height:20px}
.more{color:var(--red)}
.news{left:94px;top:768px;width:582px;height:235px}
.item{position:absolute;left:17px;width:520px}
.item .pic{float:left;width:97px;height:77px;margin-right:15px;background:linear-gradient(135deg,#4a8cc8,#d7d7d7 50%,#c94f7a)}
.item h4{font-size:12px;font-weight:700;margin-bottom:2px}
.item p{font-size:11.5px;line-height:20px;width:400px;margin-left:112px}
.testimonials{left:697px;top:768px;width:281px;height:298px}
.video{position:absolute;left:0;top:0;width:281px;height:163px;background:linear-gradient(#3a2a22,#5a5048 60%,#2e2a28)}
.play{position:absolute;left:107px;top:46px;width:62px;height:62px;border:5px solid rgba(200,200,200,.7);border-radius:50%}
.play::after{content:"";position:absolute;left:20px;top:12px;border:14px solid transparent;border-left:20px solid rgba(220,220,220,.8)}
.vbar{position:absolute;left:0;top:140px;width:281px;height:23px;background:#111}
.vbar .p{position:absolute;left:0;top:0;width:32px;height:23px;background:var(--red)}
.vbar .p::after{content:"";position:absolute;left:12px;top:6px;border:6px solid transparent;border-left:9px solid #fff}
.vbar .track{position:absolute;left:42px;top:8px;width:183px;height:7px;background:#eee}
.vbar .fs{position:absolute;right:0;top:0;width:32px;height:23px;background:var(--red)}
.tquote{position:absolute;left:18px;top:175px;width:250px;font-size:11.5px;line-height:20px}
.tquote b{display:block;margin-top:2px;font-size:11.5px}
.tile{position:absolute;top:1012px;height:54px;background:linear-gradient(#2c2c2c,#050505);color:#fff;
  font-size:19px;font-weight:700;padding:14px 19px}
.tile svg{position:absolute;right:16px;top:12px}
.footer-nav{position:absolute;left:0;top:1089px;width:1076px;text-align:center;font-size:12.5px;color:#fff}
.footer-nav a{color:#fff;text-decoration:none;margin:0 8px}
.copy{position:absolute;left:0;top:1119px;width:1076px;text-align:center;font-size:10px;color:#bbb}
.foot-social{position:absolute;left:487px;top:1145px;display:flex;gap:5px}
</style>
</head>
<body>
<div class="backdrop" role="img" aria-label="Desaturated gym photo of a trainer in a blue shirt"></div>

<header class="site-header">
  <div class="brand">
    <span class="brand-mark"></span>
    <span class="brand-name">brevakor</span>
  </div>
  <div class="follow"><span>Follow Us</span>
    <i class="dot" aria-label="chatterloop"></i><i class="dot" aria-label="quibbler"></i><i class="dot" aria-label="workweave"></i><i class="dot" aria-label="clipstream"></i>
  </div>
  <div class="search">Search
    <svg width="16" height="16" viewBox="0 0 16 16"><circle cx="6.5" cy="6.5" r="5" fill="none" stroke="#888" stroke-width="1.6"/><line x1="10" y1="10" x2="14.5" y2="14.5" stroke="#888" stroke-width="1.8"/></svg>
  </div>
  <nav class="main-nav"><a>HOME</a><a>ABOUT US</a><a>GALLERY</a><a>SERVICES</a><a>NEWS</a><a>TRAINING</a><a>BLOG</a><a>CONTACT US</a></nav>
</header>

<section class="panel contact">
  <div class="bar">Contact Form</div>
  <div class="field select" style="top:54px">Choose Program</div>
  <div class="field" style="top:90px">dd - mm - yyyy</div>
  <div class="field select" style="top:126px">Number of Persons</div>
  <div class="field" style="top:164px">Email</div>
  <div class="field" style="top:200px">Phone Number</div>
  <div class="field msg" style="top:236px">Message</div>
  <div class="btn" style="left:154px;top:323px;width:86px">Book Now</div>
</section>

<section class="slider">
  <div class="slide" role="img" aria-label="Trainer and client doing a floor workout in the gym"></div>
  <div class="arrow" style="left:21px"><svg width="12" height="14" viewBox="0 0 12 14"><path d="M8 1L2 7l6 6" fill="none" stroke="#fff" stroke-width="2"/></svg></div>
  <div class="arrow" style="left:556px"><svg width="12" height="14" viewBox="0 0 12 14"><path d="M3 1l6 6-6 6" fill="none" stroke="#fff" stroke-width="2"/></svg></div>
</section>

<section class="panel services">
  <div class="panel-title" style="width:205px">Our Services</div>
  <ul>
    <li><i></i>Personal training</li><li><i></i>Motivational speaking</li><li><i></i>Bootcamp conditioning</li>
    <li><i></i>Rondalo</li><li><i></i>Kickboxing cardio</li><li><i></i>Hip Hop Cordio</li>
  </ul>
  <div class="corner"></div>
</section>

<section class="panel gallery">
  <div class="panel-title" style="width:205px">Photo Gallery</div>
  <div class="thumb" role="img" aria-label="Workout photo" style="left:16px;top:18px"></div>
  <div class="thumb alt" role="img" aria-label="Trainer photo" style="left:104px;top:18px"></div>
  <div class="thumb alt" role="img" aria-label="Push-up photo" style="left:191px;top:18px"></div>
  <div class="thumb" role="img" aria-label="Workout photo" style="left:16px;top:91px"></div>
  <div class="thumb alt" role="img" aria-label="Trainer photo" style="left:104px;top:91px"></div>
  <div class="thumb" role="img" aria-label="Workout photo" style="left:191px;top:91px"></div>
  <div class="corner"></div>
</section>

<section class="panel training">
  <div class="panel-title" style="width:205px">Training</div>
  <div class="prog" style="top:18px"><div class="thumb" role="img" aria-label="Program photo"></div><h4>Brevakor Program</h4><p>Lorem Ipsum is simply dummy text of the printing industry. <span class="more">[+]</span></p></div>
  <div class="prog" style="top:90px"><div class="thumb" role="img" aria-label="Program photo"></div><h4>Latest Program</h4><p>Lorem Ipsum is simply dummy text of the printing industry. <span class="more">[+]</span></p></div>
  <div class="corner"></div>
</section>

<section class="panel news">
  <div class="panel-title" style="width:205px">News/Events</div>
  <div class="item" style="top:15px"><div class="pic" role="img" aria-label="Group fitness class"></div><h4>Lorem Ipsum is simply</h4><p style="margin-left:0">Lorem Ipsum is simply dummy text of the printing and typesetting industry. Lorem Ipsum has been the industry's standard dummy text ever since the 1500s, <span class="more">[+]</span></p></div>
  <div class="item" style="top:109px"><div class="pic" role="img" aria-label="Cardio machine workout"></div><h4>Lorem Ipsum is simply</h4><p style="margin-left:0">Lorem Ipsum is simply dummy text of the printing and typesetting industry. Lorem Ipsum has been the industry's standard dummy text ever since the 1500s, <span class="more">[+]</span></p></div>
  <div class="btn" style="left:18px;top:194px;width:96px">View All News</div>
</section>

<section class="panel testimonials">
  <div class="panel-title" style="width:205px">Testimonials</div>
  <div class="video" role="img" aria-label="Video of a group dance fitness class"></div>
  <div class="play"></div>
  <div class="vbar"><div class="p"></div><div class="track"></div><div class="fs"></div></div>
  <p class="tquote">Lorem Ipsum is simply dummy text of the printing and typesetting industry. Lorem Ipsum has been the industry's standard dummy text ever since the 1500s,<b>brevakor with RONDALO!!!!</b></p>
  <div class="corner"></div>
</section>

<div class="tile" style="left:94px;width:274px">FAQ’S
  <svg width="22" height="32" viewBox="0 0 22 32"><path d="M3 9a8 8 0 1 1 11 7c-2 1-3 2-3 5" fill="none" stroke="#fff" stroke-width="4"/><circle cx="11" cy="28" r="2.6" fill="#fff"/></svg>
</div>
<div class="tile" style="left:378px;width:298px">Store
  <svg width="30" height="28" viewBox="0 0 30 28"><path d="M10 2l-8 5 3 6 4-2v15h12V11l4 2 3-6-8-5c-1 3-3 4-5 4s-4-1-5-4z" fill="none" stroke="#fff" stroke-width="1.6"/></svg>
</div>

<nav class="footer-nav"><a>Home</a><a>About Us</a><a>Gallery</a><a>Services</a><a>News</a><a>Training</a><a>Blog</a><a>Contact Us</a></nav>
<div class="copy">BREVAKOR. © 2013. PRIVACY POLICY</div>
<div class="foot-social"><i class="dot" aria-label="chatterloop"></i><i class="dot" aria-label="quibbler"></i><i class="dot" aria-label="workweave"></i><i class="dot" aria-label="clipstream"></i></div>
</body>
</html>
```